Psychotherapist's business card

I need a business card design for a psychotherapist. I expect business card to have "light" design. By this I mean that it can somehow translate easiness, serenity. Maybe pastel colours can help you here. I have attached some pictures from Greece. Perhaps they can inspire you to combine colours and to achieve that "light" design.
Updates

Pls, don't use any free samples you may find on business card generators. It looks too simple, uncreative and waste of time! READ size and colour requirements! I don't want to see any shapes like rings, triangles etc.

Contact Information for Business Card

Size: 65mmX60mm

Name - Мирослав Гречихин

Психолог
+7(916)482-39-07
grechikhin.com

I suppose that thin font can look good but it's up to you

Requirements
Must have
• size requirements
Nice to have
• pastel colours
• thin font
Should not have
• black and dark colours
• lines, free design samples used from other web-sites

```html
<!DOCTYPE html>
<html lang="ru">
<head>
<meta charset="utf-8">
<title>Мирослав Гречихин — Психолог</title>
<link rel="stylesheet" href="https://fonts.googleapis.com/css2?family=PT+Sans&display=swap">
<style>
  :root {
    --bg-light: #ecf5e0;
    --bg-mid: #dbe6cf;
    --bg-deep: #c3d6be;
    --ink: #3d86f2;
    --edge: #b7bfb3;
  }
  html, body {
    margin: 0;
    padding: 0;
    width: 1200px;
    height: 1108px;
    overflow: hidden;
    background: #ffffff;
  }
  .card {
    position: relative;
    width: 1200px;
    height: 1108px;
    box-sizing: border-box;
    border: 2px solid var(--edge);
    background: linear-gradient(135deg, var(--bg-light) 0%, var(--bg-mid) 48%, var(--bg-deep) 100%);
    font-family: "PT Sans", "Trebuchet MS", sans-serif;
    color: var(--ink);
    text-align: center;
  }
  .card__name {
    position: absolute;
    top: 412px;
    left: 0;
    right: 0;
    margin: 0;
    font-size: 66px;
    font-weight: 400;
    line-height: 1.2;
    letter-spacing: 1px;
    word-spacing: 8px;
  }
  .card__role {
    position: absolute;
    top: 500px;
    left: 0;
    right: 0;
    margin: 0;
    font-size: 66px;
    font-weight: 400;
    line-height: 1.2;
    letter-spacing: 1px;
  }
  .card__contacts {
    position: absolute;
    top: 628px;
    left: 0;
    right: 0;
    display: flex;
    justify-content: center;
    align-items: center;
    gap: 28px;
    font-size: 38px;
    line-height: 1;
  }
  .card__dot {
    width: 20px;
    height: 20px;
    border-radius: 50%;
    background: var(--ink);
  }
</style>
</head>
<body>
  <main class="card">
    <h1 class="card__name">Мирослав Гречихин</h1>
    <p class="card__role">Психолог</p>
    <div class="card__contacts">
      <span class="card__phone">+7(916)482-39-07</span>
      <span class="card__dot" aria-hidden="true"></span>
      <span class="card__site">grechikhin.com</span>
    </div>
  </main>
</body>
</html>
```